Brackwell Powerpoint Template

We need a .pptx template for company presentations.

It is comprised of only two pages:

1) cover page
2) inside pages

Both pages should be based on our logo, attached on the brief.

The cover page must have space for title and subtitle.
Updates

Update on the brief:

We are looking for a cover page that is not too "busy" or complicated. Dark background is preferred, especially if it plays with the logo colors (maybe playing with a negative version of it).

The inside page has also to be simple: no arrows or anything similar. Keep in mind that those presentations will be printed in paper.

The inside page should have the logo either on the top right corner or on the bottom right corner.

A good way to separate the title (or to create space for it) would be to play with the horizon line from the logo maybe a thinner version of it, since it will have to be much longer).

The inside page must have a white background and a place for the page number.

Target Market(s)

High end investors

Industry/Entity Type

It Company

```html
<!DOCTYPE html>
<html lang="en">
<head>
<meta charset="utf-8">
<title>Brackwell – Cover</title>
<link rel="stylesheet" href="https://fonts.googleapis.com/css2?family=Old+Standard+TT:wght@400&family=Carlito:wght@400&display=swap">
<style>
  :root {
    --bg-dark: #262626;
    --brand-blue: #0078aa;
    --ink-white: #ffffff;
    --body-grey: #a9a9a9;
    --footer-text: #d6ebf5;
    --serif: "Old Standard TT", "Times New Roman", serif;
    --sans: "Carlito", "Calibri", sans-serif;
  }
  * { margin: 0; padding: 0; box-sizing: border-box; }
  html, body { width: 1200px; height: 900px; overflow: hidden; background: var(--bg-dark); }
  .cover {
    position: relative;
    width: 1200px;
    height: 900px;
    background: var(--bg-dark);
    overflow: hidden;
  }
  .title {
    position: absolute;
    left: 0; top: 0;
    font-family: var(--serif);
    font-weight: 400;
    line-height: 1;
    white-space: nowrap;
  }
  .title-line { position: absolute; display: block; }
  .white { color: var(--ink-white); }
  .blue { color: var(--brand-blue); }
  .title-main { left: 120px; top: 183px; font-size: 81px; letter-spacing: 1.5px; }
  .title-sub { left: 120px; top: 255px; font-size: 41px; letter-spacing: 0.3px; }
  .title-big { left: 119px; top: 296px; font-size: 91px; }
  .title-write { left: 549px; top: 304px; font-size: 29px; }
  .title-here { left: 549px; top: 343px; font-size: 29px; letter-spacing: 0.3px; }

  .intro {
    position: absolute;
    left: 138px;
    top: 446px;
    width: 582px;
    font-family: var(--sans);
    font-size: 15.5px;
    line-height: 22px;
    color: var(--body-grey);
  }

  .footer {
    position: absolute;
    left: 0;
    top: 729px;
    width: 1200px;
    height: 171px;
    background: var(--brand-blue);
  }
  .contact {
    position: absolute;
    left: 143px;
    top: 33px;
    font-family: var(--sans);
    font-style: normal;
    color: var(--footer-text);
  }
  .contact-heading {
    font-size: 14.5px;
    color: var(--ink-white);
    margin-bottom: 19px;
  }
  .contact-lines {
    list-style: none;
    font-size: 12.5px;
    line-height: 16px;
  }
  .contact-lines .label { display: inline-block; width: 44px; }

  .brand {
    position: absolute;
    left: 850px;
    top: 62px;
    display: flex;
    align-items: center;
    gap: 12px;
    font-family: var(--sans);
    font-weight: 400;
    font-size: 32px;
    line-height: 1;
    color: var(--ink-white);
  }
  .brand-mark {
    width: 14px;
    height: 14px;
    background: var(--ink-white);
  }
</style>
</head>
<body>
  <main class="cover">
    <h1 class="title">
      <span class="title-line title-main"><span class="white">SAMPLE</span> <span class="blue">TEXT</span></span>
      <span class="title-line title-sub white">FOR BRACKWELL TEMPLATE</span>
      <span class="title-line title-big blue">YOU CAN</span>
      <span class="title-line title-write white">WRITE</span>
      <span class="title-line title-here blue">TITLE HERE</span>
    </h1>

    <p class="intro">Duis autem vel eum iriure dolor in hendrerit in vulputate velit esse molestie consequat, vel illum dolore eu feugiat nulla facilisis at vero eros et accumsan et iusto odio loremo.</p>

    <footer class="footer">
      <address class="contact">
        <p class="contact-heading">Contact Us</p>
        <ul class="contact-lines">
          <li>48 Harlow Street</li>
          <li>Fenmore, CA 95012-4410</li>
          <li><span class="label">Phone:</span>(555) 014-2280</li>
          <li>www.brackwellcapitalpartners.com</li>
        </ul>
      </address>
      <div class="brand">
        <span class="brand-mark" aria-hidden="true"></span>
        <span class="brand-name">Brackwell</span>
      </div>
    </footer>
  </main>
</body>
</html>
```